Contemporary new French wine brand needs logo and series of label design

to design a new contemporary logo and series of labels for a new French wine brand. We hope to attract not just current French wine drinkers but new ones who may appreciate a less traditional and more modern style.

Reason: we are wanting to extend the project for a few days more to receive more submissions since we had fewer designs submitted than we were expecting, maybe because of the holidays.

Target Market(s)

people who follow the arts community (eg. music, theatre, visual/video arts, dance) --- all mature ages.

Industry/Entity Type

French Wine

Requirements
Must have
• a clear, memorable treatment for the name BRUMAIS with accompanying logo.
Nice to have
• embossing, matte/gloss refinement, tasteful foil stamping, coated stock for the whites to help the integrity of the paper in and out of ice buckets. A combo of say, three types of fonts; a semi custom font for the brand name Brumais and maybe a script and one other.
Should not have
• not traditional French

```html
<!DOCTYPE html>
<html lang="en">
<head>
<meta charset="utf-8">
<title>Brumais – Bordeaux Red Wine Label</title>
<link rel="stylesheet" href="https://fonts.googleapis.com/css2?family=Josefin+Sans:wght@300;400;600&family=Pinyon+Script&display=swap">
<style>
  :root {
    --backdrop: #e9e9e7;
    --label-paper: #fafaf9;
    --wine: #6b3a35;
    --script-wine: #7a2a2e;
    --slate: #4a4a4a;
    --mist: #adadad;
    --fine-print: #3a3a3a;
  }

  * { box-sizing: border-box; margin: 0; padding: 0; }

  html, body {
    width: 1200px;
    height: 1000px;
    overflow: hidden;
  }

  body {
    background: var(--backdrop);
    position: relative;
    font-family: "Josefin Sans", "Helvetica Neue", Arial, sans-serif;
  }

  .wine-label {
    position: absolute;
    left: 230px;
    top: 100px;
    width: 740px;
    height: 800px;
    background: var(--label-paper);
    box-shadow: 0 1px 2px rgba(0, 0, 0, 0.08);
    overflow: hidden;
  }

  .brand-lockup {
    position: absolute;
    left: 221px;
    top: 70px;
    width: 370px;
    display: flex;
    flex-direction: column;
    align-items: flex-start;
    gap: 34px;
  }

  .brand-lockup__square {
    width: 190px;
    height: 190px;
    background: var(--mist);
  }

  .brand-lockup__name {
    font-family: "Josefin Sans", "Helvetica Neue", Arial, sans-serif;
    font-weight: 400;
    font-size: 62px;
    letter-spacing: 0.08em;
    color: var(--wine);
    line-height: 1;
    white-space: nowrap;
  }

  .brand-vertical {
    position: absolute;
    left: 648px;
    top: 481px;
    transform: translate(-50%, -50%) rotate(-90deg);
    font-family: "Josefin Sans", "Helvetica Neue", Arial, sans-serif;
    font-weight: 400;
    font-size: 78px;
    letter-spacing: 0.45em;
    padding-left: 0.45em;
    color: var(--slate);
    white-space: nowrap;
    line-height: 1;
  }

  .wine-type {
    position: absolute;
    left: 354px;
    top: 641px;
    transform: translate(-50%, -50%);
    font-family: "Pinyon Script", "Brush Script MT", cursive;
    font-size: 40px;
    color: var(--script-wine);
    white-space: nowrap;
  }

  .origin {
    position: absolute;
    left: 354px;
    top: 684px;
    transform: translate(-50%, -50%);
    font-weight: 300;
    font-size: 16px;
    letter-spacing: 0.32em;
    color: var(--slate);
    white-space: nowrap;
  }

  .legal {
    position: absolute;
    left: 354px;
    top: 742px;
    transform: translateX(-50%);
    text-align: center;
    font-weight: 600;
    font-size: 10px;
    letter-spacing: 0.12em;
    line-height: 1.6;
    color: var(--fine-print);
  }
</style>
</head>
<body>
  <main class="wine-label">
    <div class="brand-lockup">
      <span class="brand-lockup__square"></span>
      <span class="brand-lockup__name">BRUMAIS</span>
    </div>

    <div class="brand-vertical">BRUMAIS</div>

    <p class="wine-type">Bordeaux Red Wine</p>
    <p class="origin">PRODUCT OF FRANCE</p>

    <p class="legal">ALC 15% BY VOL<br>750 ML</p>
  </main>
</body>
</html>
```